Letterhead Design for Law Firm that Specializes in Property Damage Litigation

We are looking for a redesign of our letterhead. Our current letterhead lists all of our current staff members and we'd like to come up with a design that does NOT list all of the staff members so that it does not need to be updated with every newly hired employee. Must be in editable format.

We are a law firm that specializes in property damage, so we need something that is professional, yet modern. The final design should use our existing logo and should use a blue color scheme (alternate colors would be gray, black, and white).

Industry/Entity Type

Legal

Colors
0054AA
0677BA
7BADD7
CADEEF
E8F1F8

```html
<!DOCTYPE html>
<html lang="en">
<head>
<meta charset="utf-8">
<title>Hartwell Ames Corbin — Letterhead</title>
<link rel="stylesheet" href="https://fonts.googleapis.com/css2?family=Poppins:wght@300;400;500;600&family=Cinzel:wght@700&display=swap">
<style>
  :root {
    --navy: #00315f;
    --ink: #0b3a6b;
    --paper: #ffffff;
    --backdrop: #ffffff;
  }
  * { margin: 0; padding: 0; box-sizing: border-box; }
  html, body {
    width: 955px; height: 1200px; overflow: hidden;
    background: var(--backdrop);
    font-family: "Poppins", sans-serif;
    color: var(--ink);
  }
  .letterhead {
    position: absolute; left: 62px; top: 62px;
    width: 831px; height: 1073px;
    background: var(--paper);
    box-shadow: 0 0 40px rgba(0,0,0,0.35);
    overflow: hidden;
  }
  .brand {
    position: absolute; left: 116px; top: 118px;
    display: flex; align-items: center; gap: 8px;
  }
  .brand-mark {
    width: 12px; height: 12px;
    background: var(--navy);
  }
  .brand-name {
    font-family: "Poppins", sans-serif; font-weight: 600;
    font-size: 13px; line-height: 16px; color: var(--navy);
  }
  .office {
    position: absolute; left: 518px; top: 112px;
  }
  .office-title {
    font-family: "Cinzel", serif; font-weight: 700;
    font-size: 12.5px; letter-spacing: 1px; color: var(--navy);
    margin-bottom: 8px;
  }
  .contact-list { list-style: none; }
  .contact-item {
    display: flex; align-items: center; gap: 5px;
    font-size: 8px; font-weight: 500; line-height: 8.5px;
    color: var(--navy); margin-bottom: 7px;
  }
  .contact-item svg { flex: none; }
  .recipient {
    position: absolute; left: 114px; top: 272px;
    font-size: 19px; font-weight: 300; line-height: 32px;
  }
  .letter-body {
    position: absolute; left: 114px; top: 383px; width: 603px;
    font-size: 16px; font-weight: 300; line-height: 27.6px;
  }
  .letter-line {
    display: block; white-space: nowrap;
    text-align: justify; text-align-last: justify;
  }
  .letter-line.is-last { text-align-last: left; }
  .letter-line.is-spaced { letter-spacing: 1.6px; }
  .signoff {
    position: absolute; left: 114px; top: 680px;
    font-size: 19px; font-weight: 500; color: var(--navy);
  }
  .signature {
    position: absolute; left: 116px; top: 720px;
    width: 160px; height: 18px;
  }
  .footer-band {
    position: absolute; left: 0; bottom: 0;
    width: 831px; height: 128px;
  }
</style>
</head>
<body>
  <main class="letterhead">
    <header>
      <div class="brand">
        <span class="brand-mark"></span>
        <span class="brand-name">Hartwell Ames Corbin</span>
      </div>

      <section class="office">
        <h2 class="office-title">HARBORVIEW OFFICE</h2>
        <ul class="contact-list">
          <li class="contact-item">
            <svg width="11" height="11" viewBox="0 0 11 11"><circle cx="5.5" cy="5.5" r="4.8" fill="none" stroke="#00315f"/><rect x="3.3" y="3.5" width="4.4" height="4" rx="0.8" fill="#00315f"/></svg>
            (555)014 - 2270
          </li>
          <li class="contact-item">
            <svg width="11" height="11" viewBox="0 0 11 11"><circle cx="5.5" cy="5.5" r="4.8" fill="none" stroke="#00315f"/><rect x="3.8" y="2.8" width="3.4" height="5.4" rx="0.6" fill="none" stroke="#00315f" stroke-width="0.9"/></svg>
            (555)018-4462
          </li>
          <li class="contact-item">
            <svg width="11" height="11" viewBox="0 0 11 11"><circle cx="5.5" cy="5.5" r="4.8" fill="none" stroke="#00315f"/><rect x="3" y="3.8" width="5" height="3.6" fill="none" stroke="#00315f" stroke-width="0.9"/><path d="M3 3.8 L5.5 5.8 L8 3.8" fill="none" stroke="#00315f" stroke-width="0.8"/></svg>
            Your Name@mailbox.com
          </li>
          <li class="contact-item">
            <svg width="11" height="11" viewBox="0 0 11 11"><circle cx="5.5" cy="5.5" r="4.8" fill="none" stroke="#00315f"/><path d="M5.5 8.3 C4 6.6 3.6 5.7 3.6 4.8 A1.9 1.9 0 0 1 7.4 4.8 C7.4 5.7 7 6.6 5.5 8.3 Z" fill="#00315f"/></svg>
            <span>4120 Riverside<br>Ave Dayton OH 45405</span>
          </li>
          <li class="contact-item">
            <svg width="11" height="11" viewBox="0 0 11 11"><circle cx="5.5" cy="5.5" r="4.8" fill="none" stroke="#00315f"/><circle cx="5.5" cy="5.5" r="2.6" fill="none" stroke="#00315f" stroke-width="0.8"/><path d="M2.9 5.5 H8.1 M5.5 2.9 V8.1" stroke="#00315f" stroke-width="0.7"/></svg>
            www.Your company.com
          </li>
        </ul>
      </section>
    </header>

    <section class="recipient">
      <p>Dear : .... .... ....</p>
      <p>9, mei, 2019, Indonesia</p>
    </section>

    <p class="letter-body">
      <span class="letter-line is-spaced">Lorem ipsum dolor sit amet, consectetur adipiscing elit,</span>
      <span class="letter-line">sed do eiusmod tempor incididunt ut labore et dolore magna aliqua.</span>
      <span class="letter-line">Ut enim ad minim veniam, quis nostrud exercitation ullamco laboris</span>
      <span class="letter-line">nisi ut aliquip ex ea commodo consequat. Duis aute irure dolor in</span>
      <span class="letter-line">reprehenderit in voluptate velit esse cillum dolore eu fugiat nulla pariatur.</span>
      <span class="letter-line">Excepteur sint occaecat cupidatat non proident, sunt in culpa qui officia</span>
      <span class="letter-line is-last">deserunt mollit anim id est laborum</span>
    </p>

    <p class="signoff">Director</p>
    <svg class="signature" role="img" aria-label="Handwritten signature of the director" viewBox="0 0 160 18">
      <rect x="0" y="7" width="160" height="4" rx="2" fill="#00315f"/>
    </svg>

    <svg class="footer-band" viewBox="0 0 831 128" preserveAspectRatio="none" aria-hidden="true">
      <path d="M0 37 Q415.5 -37 831 37 L831 128 L0 128 Z" fill="#00315f"/>
    </svg>
  </main>
</body>
</html>
```